Open Every Door Sports Career Conference

Open Every Door is a first-time in-person event focused on helping people of color learn about and obtain jobs and/or internships in the business of Sports. We are looking for a Power Point deck that we can use to assist in selling sponsorships in addition to providing general awareness. All of the details are included on the attached PP that was created in-house. I am looking for something more modern and up-to-date. This looks very dated and simplistic. The photos and graphics really need to focus on students of color and not white people.

```html
<!DOCTYPE html>
<html lang="en">
<head>
<meta charset="utf-8">
<title>Open Every Door Presentation</title>
<link href="https://fonts.googleapis.com/css2?family=Lato:wght@400;700;900&display=swap" rel="stylesheet">
<style>
:root{
  --navy:#2a3a93;
  --orange:#f58a3c;
  --ink:#333642;
  --muted:#6b6e78;
  --line:#f3a66c;
  --paper:#ffffff;
  --card-shadow:rgba(30,34,60,.16);
}
*{box-sizing:border-box;margin:0;padding:0}
html,body{width:1200px;height:3472px;overflow:hidden;background:var(--paper)}
body{font-family:'Lato',sans-serif;color:var(--ink);position:relative}
.slide{position:absolute;left:238px;width:724px;height:392px;background:var(--paper);
  box-shadow:22px 24px 34px rgba(0,0,0,.13);overflow:hidden}
.abs{position:absolute}
.kicker{position:absolute;left:46px;top:15px;font-size:9px;color:var(--orange);opacity:.8}
.title{position:absolute;left:46px;top:28px;font-size:22px;font-weight:900;color:var(--navy);letter-spacing:-.2px}
.title-rule{position:absolute;left:46px;top:56px;width:202px;height:1px;background:#c9cbd6}
.title-rule::before{content:"";position:absolute;left:0;top:0;width:100px;height:2px;background:var(--orange)}
.brand-mark{position:absolute;right:26px;top:14px;width:62px;font-size:9px;line-height:9px;font-weight:900;color:var(--navy);text-align:center;text-transform:uppercase}
.site{position:absolute;left:46px;top:362px;font-size:10px;color:var(--navy)}
.site-rule{position:absolute;left:46px;top:388px;width:100px;height:2px;background:var(--orange)}
.pager{position:absolute;left:628px;top:356px;height:22px;display:flex;align-items:center;font-size:10px;color:var(--navy)}
.pager i{display:block;width:1px;height:22px;background:#c9cbd6;margin:0 18px 0 10px}
/* cover */
.cover{background:linear-gradient(100deg,#e2e2e4 0%,#ece6e6 35%,#f4d9d0 60%,#f1c9ba 100%)}
.cover-photo{position:absolute;inset:0;clip-path:polygon(437px 0,724px 0,724px 392px,343px 392px);
  background:linear-gradient(160deg,#4f7a3a 0%,#8b4a3c 28%,#b85a46 55%,#9c4a3c 100%)}
.cover-logos{position:absolute;left:42px;top:98px;display:flex;align-items:center;gap:22px;font-size:15px;font-weight:900;color:#1e1f26}
.cover-logos .alt{color:var(--navy);display:flex;align-items:center;gap:5px}
.cover-logos .alt b{width:14px;height:14px;border-radius:50%;background:var(--navy);display:block}
.cover h1{position:absolute;left:42px;top:163px;font-size:26px;font-weight:700;color:#1e1f26;letter-spacing:-.3px}
.cover .sub{position:absolute;left:42px;top:200px;font-size:9px;color:#444}
.cover .meta{position:absolute;left:42px;top:280px;display:flex;align-items:center;font-size:13px;font-weight:700;color:#1e1f26}
.cover .meta span{color:var(--orange);font-weight:400;margin-left:4px}
.cover .meta i{display:block;width:1px;height:28px;background:var(--orange);margin:0 14px}
.cover .url{position:absolute;left:42px;top:361px;font-size:10px;color:var(--orange)}
.cover .topline{position:absolute;left:0;top:0;width:330px;height:2px;background:linear-gradient(90deg,var(--line),transparent)}
/* list */
.toc-row{position:absolute;width:249px;height:22px;border-bottom:2px solid var(--line);display:flex;justify-content:space-between;align-items:flex-end;padding-bottom:3px;font-size:9.5px;color:#2c2f3a}
/* cards */
.note{position:absolute;background:#fff;box-shadow:6px 8px 16px var(--card-shadow);font-size:8.5px;line-height:16px;color:#3b3e48;padding:14px 12px}
.photo{position:absolute}
.btn{position:absolute;border-radius:14px;background:var(--orange);color:#fff;font-size:8.5px;display:flex;align-items:center;justify-content:center;box-shadow:0 6px 12px rgba(245,138,60,.3)}
.panel{position:absolute;background:var(--navy);color:#fff;font-size:10px;line-height:19px;padding:16px 14px;box-shadow:8px 10px 18px rgba(20,28,80,.25)}
.panel ul{list-style:none;margin-top:6px;font-size:8.5px;line-height:16px}
.panel li{padding-left:12px;position:relative}
.panel li::before{content:"";position:absolute;left:1px;top:6px;width:4px;height:4px;border-radius:50%;background:var(--orange)}
.badge{position:absolute;border-radius:50%;background:var(--orange);border:3px solid #fff;box-shadow:0 4px 10px rgba(0,0,0,.15)}
.center-text{position:absolute;left:100px;width:524px;text-align:center;font-size:8.5px;line-height:16px;color:#3b3e48}
.center-text em{font-style:normal;color:var(--orange)}
.uni{position:absolute;top:151px;width:114px;height:99px;background:#fff;box-shadow:5px 6px 12px var(--card-shadow);display:flex;flex-direction:column;align-items:center;justify-content:center;gap:8px;font-size:10px;font-weight:700;color:var(--navy);text-align:center;line-height:12px;padding:0 6px}
.uni b{display:block;width:26px;height:26px;border-radius:50%;background:#d9dbe6}
.stat{position:absolute;top:195px;width:118px;height:159px;background:rgba(240,240,242,.9);display:flex;flex-direction:column;align-items:center;padding-top:58px;font-size:8.5px;line-height:16px;color:#3b3e48;text-align:center}
.stat .dot{width:26px;height:26px;border-radius:50%;background:var(--orange);margin-bottom:8px;display:flex;align-items:center;justify-content:center}
.social{position:absolute;left:469px;display:flex;align-items:center;gap:20px;font-size:8.5px;color:#3b3e48}
.social b{display:block;width:44px;height:44px;border-radius:50%;border:1px solid #e6e6ea;box-shadow:0 4px 10px rgba(0,0,0,.08);position:relative}
.social b::after{content:"";position:absolute;left:13px;top:13px;width:18px;height:18px;border-radius:50%;background:var(--orange)}
</style>
</head>
<body>

<!-- 1 Cover -->
<section class="slide cover" style="top:113px">
  <div class="cover-photo" role="img" aria-label="Photo of distance runners racing on a red stadium track"></div>
  <div class="topline"></div>
  <div class="cover-logos"><span>Keystone Youth</span><span class="alt"><b></b>Stadia Net</span></div>
  <h1>Open Every Door Presentation</h1>
  <div class="sub">Credential Subtittle Here</div>
  <div class="meta">Mr. Alan<span>Merritt</span><i></i>January<span>2023</span></div>
  <div class="url">openeverydoor.com</div>
</section>

<!-- 2 Presentation list -->
<section class="slide" style="top:586px">
  <div class="kicker">Open Every Door</div>
  <div class="title">Presentation List</div>
  <div class="title-rule"></div>
  <div class="brand-mark">Open<br>Every Door</div>
  <div class="toc-row" style="left:82px;top:112px"><span>COVER SLIDES</span><span>01</span></div>
  <div class="toc-row" style="left:82px;top:164px"><span>PRESENTATION LIST</span><span>02</span></div>
  <div class="toc-row" style="left:82px;top:217px"><span>What Is Open Every Door?</span><span>03</span></div>
  <div class="toc-row" style="left:82px;top:269px"><span>Why Open Every Door?</span><span>04</span></div>
  <div class="toc-row" style="left:393px;top:112px"><span>EVENT ONE</span><span>05</span></div>
  <div class="toc-row" style="left:393px;top:164px"><span>EVENT TWO</span><span>06</span></div>
  <div class="toc-row" style="left:393px;top:217px"><span>EVENT THREE</span><span>07</span></div>
  <div class="toc-row" style="left:393px;top:269px"><span>CLOSING SLIDE</span><span>08</span></div>
  <div class="site">openeverydoor.com</div><div class="site-rule"></div>
  <div class="pager">page<i></i>2</div>
</section>

<!-- 3 What is -->
<section class="slide" style="top:1050px">
  <div class="kicker">Open Every Door</div>
  <div class="title">What Is Open Every Door?</div>
  <div class="brand-mark">Open<br>Every Door</div>
  <div class="photo" role="img" aria-label="Photo of a broadcast production desk courtside at a basketball arena" style="left:71px;top:87px;width:268px;height:247px;background:linear-gradient(160deg,#5a4a44 0%,#2a2a2e 45%,#6d6e74 100%);box-shadow:6px 8px 16px var(--card-shadow)"></div>
  <div class="note" style="left:362px;top:100px;width:147px;height:121px">Open Every Door is a three-day event in October 6-8, 2023 that provides HBCU students and college students of color with opportunities to learn more about the business of sports.</div>
  <div class="note" style="left:541px;top:150px;width:149px;height:131px">The sports industry is one of the most competitive industries around, yet many don't truly understand the business of sports the vast amount of opportunities, or what to do to make it happen.</div>
  <div class="btn" style="left:419px;top:308px;width:157px;height:27px">WE AIM TO CHANGE THAT</div>
  <div class="site">openeverydoor.com</div><div class="site-rule"></div>
  <div class="pager">page<i></i>3</div>
</section>

<!-- 4 Why -->
<section class="slide" style="top:1514px">
  <div class="kicker">Our Professional Services</div>
  <div class="title">Why Open Every Door?</div>
  <div class="brand-mark">Open<br>Every Door</div>
  <div class="panel" style="left:127px;top:92px;width:223px;height:174px">Open Every Door creates a unique experience for students to learn about the sports business through:
    <ul><li>Brand &amp; Retailer Keynotes and Case Studies</li><li>Panel discussions with Industry Professionals</li><li>Interactive Workshops</li><li>Networking and More</li></ul></div>
  <div class="badge" style="left:319px;top:78px;width:50px;height:50px"></div>
  <div class="panel" style="left:384px;top:145px;width:222px;height:174px">Open Every Door enables companies to connect with students:
    <ul><li>Educate them about your company and employment opportunities</li><li>Recruit and build a candidate pipeline</li><li>Teach students about operations, process, strategic planning marketing, sales, finance</li></ul></div>
  <div class="badge" style="left:369px;top:126px;width:34px;height:34px"></div>
  <div class="site">openeverydoor.com</div><div class="site-rule"></div>
  <div class="pager">page<i></i>4</div>
</section>

<!-- 5 Dates -->
<section class="slide" style="top:1978px">
  <div class="kicker">Harborview Hotel, Baltimore, MD</div>
  <div class="title">October 6 – 8, 2023</div>
  <div class="title-rule"></div>
  <div class="brand-mark">Open<br>Every Door</div>
  <div class="center-text" style="top:89px">Baltimore is an ideal location to reach HBCU students as it is surrounded by a number of HBCU institutions:</div>
  <div class="uni" style="left:66px"><b></b>Harbor State University</div>
  <div class="uni" style="left:189px"><b></b>Linden State University</div>
  <div class="uni" style="left:313px"><b></b>Ridgeview State University</div>
  <div class="uni" style="left:437px"><b></b>Crestmont University</div>
  <div class="uni" style="left:563px"><b></b>Eastern Bay University</div>
  <div class="center-text" style="top:293px">And with the success of the 2022 Atlantic Collegiate Tournament, and its proximity to Philadelphia, Washington DC and Virginia, Baltimore is a perfect destination for HBCU students and students of color who want to <em>Open Every Door!</em></div>
  <div class="site">openeverydoor.com</div><div class="site-rule"></div>
  <div class="pager">page<i></i>5</div>
</section>

<!-- 6 Event -->
<section class="slide" style="top:2442px">
  <div class="kicker">Harborview Hotel, Baltimore, MD</div>
  <div class="title">What is Open Every Door</div>
  <div class="brand-mark">Open<br>Every Door</div>
  <div class="photo" role="img" aria-label="Photo of a packed football stadium under lights" style="left:55px;top:68px;width:612px;height:286px;background:linear-gradient(180deg,#3a3f4a 0%,#6b6f78 35%,#4e7d3e 70%,#7a9a5a 100%)"></div>
  <div class="stat" style="left:55px"><span class="dot"></span>Keynote Sessions<br>with Industry Leaders</div>
  <div class="stat" style="left:178px"><span class="dot"></span>Breakout Sessions<br>and Workshops</div>
  <div class="stat" style="left:302px"><span class="dot"></span>Individual meetings<br>between companies<br>and students</div>
  <div class="stat" style="left:425px"><span class="dot"></span>Stadium and venue<br>visits</div>
  <div class="stat" style="left:549px"><span class="dot"></span>Networking and<br>social events</div>
  <div class="site">openeverydoor.com</div><div class="site-rule"></div>
  <div class="pager">page<i></i>6</div>
</section>

<!-- 7 Closing -->
<section class="slide" style="top:2906px">
  <div class="kicker">Close Presentation</div>
  <div class="title">Closing Page</div>
  <div class="title-rule"></div>
  <div class="brand-mark">Open<br>Every Door</div>
  <div class="abs" style="left:59px;top:100px;font-size:16px;line-height:22px;color:#3b3e48"><span style="color:var(--orange)">Our Professional</span> &amp; Qualified Customer<br>Service are Available 24/7</div>
  <div class="abs" style="left:59px;top:231px;font-size:11px;color:#3b3e48">Our Address</div>
  <div class="abs" style="left:59px;top:250px;font-size:7px;line-height:13px;color:var(--muted)">Field Street No 4, Marlow Specialist<br>Centre, Rooms 2 Marlow US</div>
  <div class="abs" style="left:186px;top:213px;width:163px;height:89px;border:1px solid #f6d3b7;border-radius:6px;padding:6px">
    <div style="height:100%;box-shadow:0 4px 12px rgba(0,0,0,.1);padding:10px 14px;background:#fff">
      <div style="font-size:11px;color:#3b3e48">Phone &amp; Email</div>
      <div style="font-size:7px;line-height:13px;color:var(--muted);margin-top:4px">(02) 555 0142<br>admin@OpenEveryDoor.com</div>
    </div>
  </div>
  <div class="social" style="top:95px"><b></b>chatter.net/OpenEveryDoor/</div>
  <div class="social" style="top:151px"><b></b>snapgram.net/OpenEveryDoor/</div>
  <div class="social" style="top:207px"><b></b>OpenEveryDoor.com/</div>
  <div class="social" style="top:263px"><b></b>worknet.com/OpenEveryDoor/</div>
  <div class="site">openeverydoor.com</div><div class="site-rule"></div>
  <div class="pager">page<i></i>7</div>
</section>

</body>
</html>
```